3 x 3 metre trade booth design

We need a design for a 3 x 3 metre corner booth for a conference we are attending. There will therefore be 2 x backdrops that we need to have designed. For one of them we want to have our services displayed as an engaging, modern infographic. For the other, we would like to have our brand tagline and our logo, with a cool background which aligns with what we do.
I have attached a picture of what our booth looked like last year- we designed this ourself and we need it to look much more professional, with a different type of infographic for the
Please see attachment with full design brief attached

```html
<!DOCTYPE html>
<html lang="en">
<head>
<meta charset="utf-8">
<title>Full Service Management – Corvanta</title>
<link href="https://fonts.googleapis.com/css2?family=Roboto:wght@400;700;900&display=swap" rel="stylesheet">
<style>
  :root {
    --bg-yellow: #fbe014;
    --bg-sand: #d9a36a;
    --bg-mauve: #b06a98;
    --bg-purple: #84409c;
    --disc-yellow: #fde83c;
    --disc-gold: #fcc317;
    --disc-orange: #f39a3a;
    --disc-red: #e8403a;
    --ink: #111111;
    --white: #ffffff;
    --ring: #f5b92c;
  }
  * { margin: 0; padding: 0; box-sizing: border-box; }
  html, body { width: 1200px; height: 960px; overflow: hidden; }
  body { font-family: "Roboto", Arial, sans-serif; color: var(--ink); }

  .board {
    position: relative;
    width: 1200px;
    height: 960px;
    overflow: hidden;
    background: linear-gradient(115deg, var(--bg-yellow) 0%, var(--bg-sand) 30%, var(--bg-mauve) 58%, var(--bg-purple) 80%, var(--bg-purple) 100%);
  }

  .title {
    position: absolute;
    left: 47px;
    top: 51px;
    font-size: 21.5px;
    font-weight: 700;
    white-space: nowrap;
  }

  .brand {
    position: absolute;
    left: 932px;
    top: 31px;
    display: flex;
    align-items: center;
    gap: 20px;
  }
  .brand-square {
    width: 60px;
    height: 64px;
    border: 3px solid var(--white);
  }
  .brand-name {
    color: var(--white);
    font-weight: 900;
    font-size: 24px;
    letter-spacing: 4px;
  }

  .rings { position: absolute; inset: 0; }

  .disc {
    position: absolute;
    left: 278px;
    top: 97px;
    width: 794px;
    height: 794px;
    border-radius: 50%;
    background: linear-gradient(90deg, var(--disc-yellow) 0%, var(--disc-gold) 28%, var(--disc-orange) 65%, var(--disc-red) 100%);
  }

  .hub {
    position: absolute;
    left: 570px;
    top: 377px;
    width: 222px;
    height: 222px;
    border-radius: 50%;
    background: linear-gradient(90deg, var(--disc-yellow) 0%, var(--disc-gold) 30%, var(--disc-orange) 70%, var(--disc-red) 100%);
  }

  .service {
    position: absolute;
    font-size: 15.6px;
    line-height: 19.2px;
    white-space: nowrap;
  }
  .service h2 {
    font-size: 16.3px;
    line-height: 19.2px;
    font-weight: 700;
  }
  .service ul { list-style: none; }
  .align-center { text-align: center; transform: translateX(-50%); }
  .align-right { text-align: right; transform: translateX(-100%); }

  .icon { position: absolute; }
</style>
</head>
<body>
<div class="board">

  <svg class="rings" width="1200" height="960" viewBox="0 0 1200 960" aria-hidden="true">
    <circle cx="618" cy="482" r="445" fill="none" stroke="var(--ring)" stroke-width="0.8"/>
    <circle cx="907" cy="1230" r="473" fill="none" stroke="var(--ring)" stroke-width="0.8"/>
  </svg>

  <h1 class="title">FULL SERVICE MANAGEMENT</h1>

  <div class="brand">
    <span class="brand-square"></span>
    <span class="brand-name">CORVANTA</span>
  </div>

  <div class="disc"></div>
  <div class="hub"></div>

  <!-- Account management: clipboard with tick -->
  <svg class="icon" style="left:650px;top:119px" width="64" height="78" viewBox="0 0 64 78" aria-hidden="true">
    <rect x="4" y="8" width="56" height="68" rx="5" fill="none" stroke="var(--ink)" stroke-width="5"/>
    <rect x="20" y="2" width="24" height="12" rx="3" fill="var(--ink)"/>
    <path d="M17 42 l10 10 l20 -22" fill="none" stroke="var(--ink)" stroke-width="6" stroke-linecap="round" stroke-linejoin="round"/>
  </svg>

  <section class="service align-center" style="left:681px;top:205px">
    <h2>Account Management</h2>
    <ul>
      <li>Catalogue management</li>
      <li>Account health monitoring</li>
      <li>Case log &amp; issue resolution</li>
      <li>Multi-channel Inventory Management</li>
      <li>Customised Reporting</li>
    </ul>
  </section>

  <!-- Advertising: megaphone -->
  <svg class="icon" style="left:333px;top:336px" width="80" height="64" viewBox="0 0 80 64" aria-hidden="true">
    <rect x="4" y="20" width="14" height="22" rx="2" fill="var(--ink)"/>
    <path d="M18 20 L54 4 V58 L18 42 Z" fill="var(--ink)"/>
    <rect x="10" y="42" width="10" height="18" rx="2" fill="var(--ink)"/>
    <path d="M62 31 h14 M61 18 l12 -6 M61 44 l12 6" stroke="var(--ink)" stroke-width="4" stroke-linecap="round"/>
  </svg>

  <section class="service" style="left:333px;top:412px">
    <h2>Nexmart Advertising</h2>
    <ul>
      <li>Sponsored Ads (PPC)</li>
      <li>Bid automation</li>
      <li>Demand-Side Platform (DSP)</li>
    </ul>
  </section>

  <!-- Account setup: plain gear -->
  <svg class="icon" style="left:945px;top:330px" width="74" height="74" viewBox="0 0 82 82" aria-hidden="true">
    <g fill="var(--ink)">
      <rect x="34" y="0" width="14" height="82"/>
      <rect x="0" y="34" width="82" height="14"/>
      <rect x="34" y="0" width="14" height="82" transform="rotate(45 41 41)"/>
      <rect x="34" y="0" width="14" height="82" transform="rotate(-45 41 41)"/>
      <circle cx="41" cy="41" r="30"/>
    </g>
    <circle cx="41" cy="41" r="12" fill="var(--disc-orange)"/>
  </svg>

  <section class="service align-right" style="left:1023px;top:412px">
    <h2>Nexmart Account Setup</h2>
    <ul>
      <li>Cost analysis to scale profitably</li>
      <li>Account audit</li>
      <li>Nexmart Brand Protection</li>
    </ul>
  </section>

  <!-- International: globe -->
  <svg class="icon" style="left:370px;top:552px" width="72" height="72" viewBox="0 0 72 72" aria-hidden="true">
    <g fill="none" stroke="var(--ink)" stroke-width="4">
      <circle cx="36" cy="36" r="32"/>
      <ellipse cx="36" cy="36" rx="14" ry="32"/>
      <line x1="4" y1="36" x2="68" y2="36"/>
      <path d="M9 20 h54 M9 52 h54"/>
    </g>
  </svg>

  <section class="service" style="left:364px;top:638px">
    <h2>International Expansion</h2>
    <ul>
      <li>Market opportunity analysis</li>
      <li>Launch in new marketplaces</li>
      <li>Listing localisation</li>
      <li>Logistics &amp; Fulfilment strategy</li>
    </ul>
  </section>

  <!-- Brand content: magnifier -->
  <svg class="icon" style="left:914px;top:552px" width="72" height="72" viewBox="0 0 72 72" aria-hidden="true">
    <circle cx="28" cy="28" r="22" fill="none" stroke="var(--ink)" stroke-width="6"/>
    <line x1="44" y1="44" x2="66" y2="66" stroke="var(--ink)" stroke-width="10" stroke-linecap="round"/>
  </svg>

  <section class="service align-right" style="left:987px;top:638px">
    <h2>Brand Content &amp; Optimisation</h2>
    <ul>
      <li>Rich Content / Enhanced Product Pages</li>
      <li>Brand store</li>
      <li>Product listing optimisation</li>
      <li>Search Engine Optimisation (SEO)</li>
    </ul>
  </section>

</div>
</body>
</html>
```